Painting Company Business Card

Brightwell Painting needs a new business card. See attachments for our logo and current card as an example.
We want to utilize the same colors in the logo, and keep all the information that is currently on it. Just need an updated and modern design.
We are open to loosing the Association Logos if it means a better design.
We are also entertaining a spot for a picture of a headshot of the person listed on the card. Head shot can be finished later.

```html
<!DOCTYPE html>
<html lang="en">
<head>
<meta charset="utf-8">
<title>Brightwell Painting – Business Card</title>
<link rel="stylesheet" href="https://fonts.googleapis.com/css2?family=Fira+Sans:wght@500;600;700&display=swap">
<style>
  :root {
    --backdrop: #ecdfe0;
    --card: #ffffff;
    --forest: #404730;
    --brick: #6b3a35;
    --on-band: #ffffff;
  }
  * { box-sizing: border-box; margin: 0; padding: 0; }
  html, body { width: 1200px; height: 1200px; overflow: hidden; }
  body {
    background: var(--backdrop);
    font-family: "Fira Sans", Arial, sans-serif;
    position: relative;
  }
  .card {
    position: absolute;
    left: 209px;
    width: 780px;
    height: 480px;
    background: var(--card);
    overflow: hidden;
  }
  .card--front { top: 63px; }
  .card--back { top: 619px; }

  .wordmark {
    position: absolute;
    color: var(--forest);
    font-weight: 700;
    text-align: center;
    line-height: 0.95;
    letter-spacing: -0.01em;
  }
  .card--front .wordmark { left: 192px; width: 396px; top: 188px; font-size: 62px; }
  .card--back .wordmark { left: 225px; width: 330px; top: 86px; font-size: 44px; }

  .rule {
    position: absolute;
    top: 241px;
    width: 192px;
  }
  .rule--left { left: 0; }
  .rule--right { right: 0; }
  .rule span {
    display: block;
    height: 2px;
    background: var(--brick);
    margin-bottom: 3px;
  }
  .rule--left span:nth-child(2) { width: 186px; }
  .rule--left span:nth-child(3) { width: 186px; }
  .rule--right span:nth-child(2), .rule--right span:nth-child(3) { margin-left: 6px; }

  .band {
    position: absolute;
    left: 0;
    width: 100%;
    background: var(--forest);
    color: var(--on-band);
  }
  .card--front .band {
    top: 423px; height: 57px;
    display: flex; align-items: center; justify-content: center;
    font-size: 24px; font-weight: 600;
  }
  .card--back .band { top: 383px; height: 97px; }

  .contact { position: absolute; color: var(--forest); font-weight: 600; }
  .icon { position: absolute; fill: var(--forest); }
  .person-name { left: 186px; top: 251px; font-size: 18px; letter-spacing: 0.01em; }
  .person-role { left: 207px; top: 277px; font-size: 11px; }
  .phone-number { left: 189px; top: 316px; font-size: 18px; }
  .email { left: 448px; top: 256px; font-size: 18px; }
  .website { left: 448px; top: 313px; font-size: 18px; }
  .divider {
    position: absolute;
    left: 364px; top: 255px;
    width: 1.5px; height: 88px;
    background: var(--brick);
  }

  .services { list-style: none; }
  .services li {
    position: absolute;
    top: 36px;
    font-size: 13px;
    font-weight: 600;
    display: flex; align-items: center;
  }
  .services li::before {
    content: "";
    width: 10px; height: 10px;
    background: var(--on-band);
    margin-right: 10px;
  }
</style>
</head>
<body>

<section class="card card--front">
  <div class="rule rule--left"><span></span><span></span><span></span></div>
  <div class="wordmark">Brightwell<br>Painting</div>
  <div class="rule rule--right"><span></span><span></span><span></span></div>
  <div class="band">BrightwellPainting.com</div>
</section>

<section class="card card--back">
  <div class="wordmark">Brightwell<br>Painting</div>

  <svg class="icon" style="left:139px;top:248px" width="31" height="30" viewBox="0 0 31 30" aria-hidden="true">
    <circle cx="15.5" cy="8" r="7.5"/>
    <path d="M0 30 C1 20 7 17 15.5 17 C24 17 30 20 31 30 Z"/>
  </svg>
  <div class="contact person-name">MARK ELLISON</div>
  <div class="contact person-role">QUALITY MANAGER</div>

  <svg class="icon" style="left:145px;top:315px" width="28" height="33" viewBox="0 0 24 28" aria-hidden="true">
    <path d="M5 1 L9 7 C9.6 8 9.4 9 8.6 9.6 L6.8 11 C8 15 11 19.5 14.6 21.8 L16.4 20.4 C17.2 19.8 18.3 19.9 19 20.7 L23 25 C23.6 25.8 23.4 26.8 22.6 27.3 C20 29 16.5 28.6 13.5 26 C8 21.5 3.5 14.5 1.5 8 C0.5 4.8 1.5 2.2 3.5 0.8 C4 0.5 4.6 0.5 5 1 Z"/>
  </svg>
  <div class="contact phone-number">555-014-2260</div>

  <div class="divider"></div>

  <svg class="icon" style="left:405px;top:259px" width="31" height="22" viewBox="0 0 31 22" aria-hidden="true">
    <path d="M0 0 H31 V22 H0 Z M2.5 2 L15.5 12.5 L28.5 2 Z M2 4 V20 H29 V4 L15.5 15 Z" fill-rule="evenodd"/>
  </svg>
  <div class="contact email">mark@brightwellpainting.com</div>

  <svg class="icon" style="left:405px;top:309px" width="32" height="32" viewBox="0 0 32 32" fill="none" stroke="#404730" stroke-width="1.5" aria-hidden="true">
    <circle cx="16" cy="16" r="14.5"/>
    <ellipse cx="16" cy="16" rx="6.5" ry="14.5"/>
    <line x1="16" y1="1.5" x2="16" y2="30.5"/>
    <line x1="1.5" y1="16" x2="30.5" y2="16"/>
    <path d="M4 8.5 H28 M4 23.5 H28"/>
  </svg>
  <div class="contact website">BrightwellPainting.com</div>

  <div class="band">
    <ul class="services">
      <li style="left:148px">Exterior Painting</li>
      <li style="left:301px">Interior Painting</li>
      <li style="left:452px">Carpentry</li>
      <li style="left:567px">Drywall</li>
    </ul>
  </div>
</section>

</body>
</html>
```